Redesign (8 documents) attached with brand guidelines - very quick/easy job!

We have 8 flyers/documents that we need put into the style of our new brand (see attached). So this is a simple rebrand exercise - complete with our brand guidelines (see attached)

I would need the designer to sign an NDA prior to taking this piece of work as I will be sharing newly branded documents with you prior to market release.

If these are done well we would as the same designer to work on a z-card designed brochure/POS

Brief:

- These are documents that customers would need to complete in order to book a particular service
- If you use images (ideally from Pixvane, so we don’t have to pay for them!)
- Icon ideas enclosed
-All the content on the brochures is required: but if you think it would 'flow better' in a different order that is fine.

Target Market(s)

Customers interested in receiving a particular service

Industry/Entity Type

Work

Other font styles liked:
• Brandon (see brand guide)

Requirements
Must have
• A4
Nice to have
• New logo ideas
Should not have
• Anything out of brand guidleines

```html
<!DOCTYPE html>
<html lang="en">
<head>
<meta charset="utf-8">
<title>Vitalora – Health Objectives</title>
<link href="https://fonts.googleapis.com/css2?family=Titillium+Web:wght@400;600;700&display=swap" rel="stylesheet">
<style>
  :root {
    --teal: #1a9bc0;
    --yellow: #f2e317;
    --frame: #c9c9cb;
    --ink: #3a3a3a;
    --muted: #6b6b6b;
    --paper: #ffffff;
    --backdrop: #e9e9e9;
  }
  * { box-sizing: border-box; margin: 0; padding: 0; }
  html, body {
    width: 864px; height: 1200px; overflow: hidden;
    background: var(--backdrop);
    font-family: "Titillium Web", Arial, sans-serif;
    color: var(--ink);
  }
  .sheet-holder {
    position: absolute; left: 7.6px; top: 0;
    width: 505px; height: 714px;
    transform: scale(1.6807); transform-origin: 0 0;
  }
  .sheet {
    position: relative; width: 505px; height: 714px;
    background: var(--paper); overflow: hidden;
  }
  .sheet-shapes { position: absolute; inset: 0; width: 505px; height: 714px; }
  .texture {
    position: absolute; left: 20px; top: 60px; width: 220px; height: 220px;
    background: radial-gradient(closest-side, rgba(200,200,205,.35), rgba(255,255,255,0));
  }
  .texture-bottom {
    position: absolute; left: 170px; top: 620px; width: 260px; height: 120px;
    background: radial-gradient(closest-side, rgba(200,200,205,.3), rgba(255,255,255,0));
  }
  .brand {
    position: absolute; left: 34px; top: 30px;
    display: flex; align-items: center; gap: 6px;
  }
  .brand-mark { width: 12px; height: 12px; border-radius: 50%; background: var(--paper); }
  .brand-name {
    font-size: 21px; font-weight: 600; color: var(--paper); line-height: 1;
  }
  .doc-title {
    position: absolute; right: 42px; top: 101px;
    font-size: 14px; font-weight: 700; color: var(--teal);
  }
  .field {
    position: absolute; font-size: 7px; font-weight: 600; color: var(--muted);
    display: flex; align-items: flex-end; white-space: nowrap;
  }
  .field .fill { flex: 1; border-bottom: 1px dotted #9a9a9a; margin-left: 2px; height: 6px; }
  .field-nutritionist { left: 251px; top: 143px; width: 212px; }
  .field-store { left: 251px; top: 171px; width: 212px; }
  .field-date { left: 251px; top: 199px; width: 212px; }
  .field-client { left: 41px; top: 199px; width: 197px; }

  .reason-table {
    position: absolute; left: 40px; width: 425px;
    background: var(--frame); border-radius: 8px; padding: 2px;
  }
  .reason-1 { top: 220px; }
  .reason-2 { top: 452px; }
  .reason-head {
    height: 21px; background: var(--teal); border-radius: 7px 7px 0 0;
    display: flex; align-items: center;
    font-size: 8px; font-weight: 700; color: var(--paper);
  }
  .reason-head .label { width: 148px; padding-left: 10px; }
  .reason-head .comments { padding-left: 10px; }
  .reason-row { display: flex; gap: 1px; height: 50px; margin-top: 1px; }
  .reason-row .question {
    width: 150px; background: var(--paper); border-radius: 5px;
    padding: 9px 22px 8px 10px; font-size: 6px; line-height: 1.45; color: var(--muted);
  }
  .reason-row .answer { flex: 1; background: var(--paper); border-radius: 5px; }
  .reason-row.tall { height: 52px; }
</style>
</head>
<body>
<div class="sheet-holder">
  <div class="sheet">
    <div class="texture" role="img" aria-label="Soft grey abstract background shapes"></div>
    <div class="texture-bottom" role="img" aria-label="Soft grey abstract background shapes"></div>

    <svg class="sheet-shapes" viewBox="0 0 505 714" aria-hidden="true">
      <path d="M0,0 H505 V8 C380,24 160,60 0,165 Z" fill="var(--teal)"/>
      <path d="M0,165 C160,60 380,24 505,8 V14 C380,34 160,82 0,188 Z" fill="var(--yellow)"/>
      <path d="M372,714 C425,700 470,688 505,668 V714 Z" fill="var(--teal)"/>
      <path d="M345,714 C415,698 468,680 505,654 V668 C470,688 425,700 372,714 Z" fill="var(--yellow)"/>
    </svg>

    <div class="brand">
      <span class="brand-mark"></span>
      <span class="brand-name">Vitalora</span>
    </div>

    <h1 class="doc-title">Health Objectives</h1>

    <div class="field field-nutritionist">Nutritionist’s name:<span class="fill"></span></div>
    <div class="field field-store">Store location:<span class="fill"></span></div>
    <div class="field field-date">Date of consultation:<span class="fill"></span></div>
    <div class="field field-client">Client’s name:<span class="fill"></span></div>

    <section class="reason-table reason-1">
      <div class="reason-head"><span class="label">Reason 1</span><span class="comments">Your comments</span></div>
      <div class="reason-row"><div class="question">Symptom, issue or condition you want to address.</div><div class="answer"></div></div>
      <div class="reason-row"><div class="question">Duration - how long have you felt like this or experienced this symptom(s)?</div><div class="answer"></div></div>
      <div class="reason-row"><div class="question">Have you seen a doctor about this for a diagnosis? Did you receive any medical treatment?</div><div class="answer"></div></div>
      <div class="reason-row tall"><div class="question">Is there any background or extra health or lifestyle information that relates to this situation that you want your practitioner to know about? Please give details.</div><div class="answer"></div></div>
    </section>

    <section class="reason-table reason-2">
      <div class="reason-head"><span class="label">Reason 2</span><span class="comments">Your comments</span></div>
      <div class="reason-row"><div class="question">Symptom, issue or condition you want to address.</div><div class="answer"></div></div>
      <div class="reason-row"><div class="question">Duration - how long have you felt like this or experienced this symptom(s)?</div><div class="answer"></div></div>
      <div class="reason-row"><div class="question">Have you seen a doctor about this for a diagnosis? Did you receive any medical treatment?</div><div class="answer"></div></div>
      <div class="reason-row tall"><div class="question">Is there any background or extra health or lifestyle information that relates to this situation that you want your practitioner to know about? Please give details.</div><div class="answer"></div></div>
    </section>
  </div>
</div>
</body>
</html>
```